Stylish Business Cards Wanted

- DOUBLE SIDED Design Required -

High end, edgy cards for a corporate and personal stylist. Must include logo,
Name: Belinda Forsey
Title: Director and Stylist
telephone : +61 8 8217 4592
email: belinda@thegarbledger.example
website: thegarbledger.example
Tag: Corporate Workwear & Uniform Specialist | Personal Stylist
Would like nice icons for telephone, email, website

Target Market(s)

Businesses wanting stylish uniforms, people wanting stylish wardrobes

Industry/Entity Type

Corporate Workwear Stylist

Contact Information for Business Card

I would like black, white and gold foiling incorporated in the design - possibly a touch of the other colours on my branding guide attached Name: Belinda Forsey Title: Director and Stylist telephone : +61 8 8217 4592 email: belinda@thegarbledger.example website: thegarbledger.example Tag: Corporate Workwear & Uniform Specialist | Personal Stylist Would like nice icons for telephone, email, website

Font styles to use
Other font styles liked:
• Raleway

Colors

Designer to choose colors to be used in the design.

Requirements
Must have
• Gold foil accents

```html
<!DOCTYPE html>
<html lang="en">
<head>
<meta charset="utf-8">
<title>The Garb Ledger – Business Card</title>
<link href="https://fonts.googleapis.com/css2?family=Raleway:wght@500;700;800&display=swap" rel="stylesheet">
<style>
  :root {
    --page-bg: #e9e4dd;
    --card-bg: #f3ece2;
    --card-edge: #ddd2c3;
    --ink: #1d1b19;
    --gold: #c9a13b;
  }
  html, body {
    margin: 0;
    width: 1200px;
    height: 863px;
    overflow: hidden;
    background: var(--page-bg);
    font-family: "Raleway", sans-serif;
    color: var(--ink);
  }
  .business-card {
    position: absolute;
    left: 150px;
    top: 161px;
    width: 900px;
    height: 540px;
    box-sizing: border-box;
    border-radius: 36px;
    background: var(--card-bg);
    border: 1px solid var(--card-edge);
  }
  .brand-name {
    position: absolute;
    left: 70px;
    top: 170px;
    width: 300px;
    text-align: center;
    font-weight: 800;
    font-size: 42px;
    line-height: 1.1;
    color: var(--ink);
  }
  .divider {
    position: absolute;
    left: 405px;
    top: 120px;
    width: 2px;
    height: 230px;
    background: var(--ink);
  }
  .contact-block {
    position: absolute;
    left: 450px;
    top: 130px;
  }
  .person-name {
    margin: 0;
    font-weight: 800;
    font-size: 42px;
    line-height: 1.1;
  }
  .person-title {
    margin: 4px 0 28px;
    font-weight: 500;
    font-size: 19px;
    color: var(--gold);
  }
  .contact-list {
    list-style: none;
    margin: 0;
    padding: 0;
  }
  .contact-item {
    display: flex;
    align-items: center;
    gap: 16px;
    font-weight: 500;
    font-size: 21px;
    margin-bottom: 14px;
  }
  .contact-icon {
    width: 22px;
    height: 22px;
    flex: none;
  }
  .tagline {
    position: absolute;
    left: 70px;
    bottom: 56px;
    margin: 0;
    font-weight: 500;
    font-size: 24px;
  }
</style>
</head>
<body>
  <article class="business-card">
    <div class="brand-name">The Garb Ledger</div>
    <div class="divider"></div>

    <section class="contact-block">
      <h1 class="person-name">Belinda Forsey</h1>
      <p class="person-title">Director and Stylist</p>
      <ul class="contact-list">
        <li class="contact-item">
          <svg class="contact-icon" viewBox="0 0 24 24" aria-hidden="true">
            <path fill="#1d1b19" d="M6.6 10.8a15.2 15.2 0 0 0 6.6 6.6l2.2-2.2a1 1 0 0 1 1-.25 11.4 11.4 0 0 0 3.6.57 1 1 0 0 1 1 1V20a1 1 0 0 1-1 1A17 17 0 0 1 3 4a1 1 0 0 1 1-1h3.5a1 1 0 0 1 1 1c0 1.25.2 2.45.57 3.57a1 1 0 0 1-.25 1z"/>
          </svg>
          <span>+61 8 8217 4592</span>
        </li>
        <li class="contact-item">
          <svg class="contact-icon" viewBox="0 0 24 24" aria-hidden="true">
            <rect x="2" y="5" width="20" height="14" rx="1.5" fill="#1d1b19"/>
            <path d="M3 6.5l9 6.5 9-6.5" fill="none" stroke="#f3ece2" stroke-width="1.6"/>
          </svg>
          <span>belinda@thegarbledger.example</span>
        </li>
        <li class="contact-item">
          <svg class="contact-icon" viewBox="0 0 24 24" aria-hidden="true">
            <circle cx="12" cy="12" r="10" fill="#1d1b19"/>
            <ellipse cx="12" cy="12" rx="4" ry="10" fill="none" stroke="#f3ece2" stroke-width="1.3"/>
            <path d="M2.5 12h19M4 7h16M4 17h16" stroke="#f3ece2" stroke-width="1.3"/>
          </svg>
          <span>www.thegarbledger.example</span>
        </li>
      </ul>
    </section>

    <p class="tagline">Corporate Workwear &amp; Uniform Specialist | Personal Stylist</p>
  </article>
</body>
</html>
```